Poster Design Project- kids dancing/sport

I need a poster design for a childrens dance and sport program!!
I have attached a brochure and logo designs. From the brochure please include information from sections titled "twirl'n'hop" and "themes". Also please put on the phone number and email address (found on the brochure). Emphasis on FUN!! Make poster colourful, very kid friendly and eye catching.
Some other things i would like on the poster are:
"Does your child love to dance, sing and play sport?? Why not enrol them in our fun-filled program?"
"From only $10.00 per class"
"Sign up for your FREE trial class today"
"A fun introduction to the joy of Dance, Sport and Music for 2-6yr olds. Held in your childcare centre!!"
Hi!!
I would like to stress its TRIAL class not TRAIL class. Please feel free to play around with the information, it doesnt need to be in one blurb. Also i have updated the brief. I would like "Does you child love to dance, sing or play sport? Why not enrol in our fun filled program?" or something to that effect!!
Thanks!!!!
2-6yr olds and their parents
Childcare

```html
<!DOCTYPE html>
<html lang="en">
<head>
<meta charset="utf-8">
<title>Twirl 'N' Hop – Dance, Sport and Music for Kids</title>
<link href="https://fonts.googleapis.com/css2?family=Anton&family=Arimo:ital,wght@0,700;1,700&family=Luckiest+Guy&display=swap" rel="stylesheet">
<style>
  :root {
    --ink: #111111;
    --paper: #ffffff;
    --yellow: #fbb829;
    --blue: #1ab0e8;
    --green: #6cbd45;
    --red: #d8303e;
    --purple: #6a3d97;
    --stripe-red: #d8303e;
    --stripe-yellow: #fcc43a;
    --stripe-green: #7cc04f;
    --stripe-blue: #3bb6e6;
    --stripe-purple: #5e3b8f;
  }
  html, body {
    margin: 0;
    padding: 0;
    width: 846px;
    height: 1200px;
    overflow: hidden;
    background: var(--paper);
  }
  .poster {
    position: relative;
    width: 846px;
    height: 1200px;
    background: var(--paper);
    font-family: "Arimo", Arial, sans-serif;
    color: var(--ink);
    overflow: hidden;
  }
  .line {
    position: absolute;
    left: 0;
    width: 100%;
    text-align: center;
    margin: 0;
    white-space: nowrap;
  }
  .question {
    top: 22px;
    font-size: 41px;
    font-style: italic;
    font-weight: 700;
  }
  .activities {
    top: 68px;
    font-family: "Anton", Impact, sans-serif;
    font-size: 86px;
    line-height: 1.1;
    letter-spacing: -1px;
  }
  .activities .dance { color: var(--yellow); }
  .activities .sing { color: var(--blue); }
  .activities .amp {
    font-family: "Arimo", Arial, sans-serif;
    color: var(--ink);
    font-size: 40px;
    vertical-align: 22px;
    margin: 0 6px;
  }
  .activities .sport { color: var(--green); }
  .enrol {
    top: 188px;
    font-size: 34px;
    font-style: italic;
    font-weight: 700;
  }
  .program-name {
    top: 256px;
    font-family: "Anton", Impact, sans-serif;
    font-size: 104px;
    line-height: 1.1;
    color: var(--red);
    letter-spacing: 2px;
  }
  .intro {
    top: 405px;
    font-size: 30px;
    font-weight: 700;
  }
  .disciplines {
    top: 442px;
    font-size: 62px;
    font-style: italic;
    font-weight: 700;
    color: var(--purple);
    letter-spacing: -1px;
  }
  .disciplines .and {
    font-style: normal;
    font-size: 36px;
    color: var(--ink);
  }
  .venue {
    top: 522px;
    font-size: 26px;
    font-style: italic;
    font-weight: 700;
  }
  .rainbow {
    position: absolute;
    left: 0;
    top: 560px;
  }
  .kids-area {
    position: absolute;
    left: 30px;
    top: 790px;
    width: 790px;
    height: 265px;
    background: linear-gradient(to bottom, rgba(0,0,0,0.0), rgba(0,0,0,0.85) 30%, rgba(0,0,0,0.9));
    border-radius: 60px 60px 0 0;
  }
  .fun-burst {
    position: absolute;
    left: 140px;
    top: 575px;
    font-family: "Luckiest Guy", "Arial Black", sans-serif;
    font-size: 118px;
    color: var(--green);
    -webkit-text-stroke: 6px var(--purple);
    paint-order: stroke fill;
    text-shadow: 0 0 0 var(--paper), 4px 4px 0 var(--paper);
    transform: rotate(-7deg);
    margin: 0;
  }
  .ages {
    position: absolute;
    left: 452px;
    top: 580px;
    width: 250px;
    text-align: center;
    font-size: 36px;
    font-weight: 700;
    line-height: 1.12;
    color: var(--red);
    transform: rotate(-4deg);
    margin: 0;
  }
  .price-badge {
    position: absolute;
    left: 660px;
    top: 660px;
    width: 170px;
    height: 170px;
    border-radius: 50%;
    background: radial-gradient(circle, rgba(255,255,255,0.45), rgba(255,255,255,0) 70%);
    text-align: center;
    font-family: "Anton", Impact, sans-serif;
    transform: rotate(8deg);
  }
  .price-badge .from {
    display: block;
    padding-top: 12px;
    font-size: 24px;
    color: var(--paper);
    -webkit-text-stroke: 1px var(--ink);
  }
  .price-badge .amount {
    display: block;
    font-size: 84px;
    line-height: 0.95;
    color: var(--yellow);
    -webkit-text-stroke: 2px var(--ink);
    paint-order: stroke fill;
  }
  .price-badge .amount sup {
    font-size: 42px;
    vertical-align: 30px;
  }
  .price-badge .per {
    display: block;
    font-size: 24px;
    color: var(--ink);
  }
  .footer-band {
    position: absolute;
    left: 14px;
    top: 1055px;
    width: 818px;
    height: 132px;
    background: var(--ink);
    color: var(--paper);
    text-align: center;
  }
  .cta {
    margin: 26px 0 0;
    font-family: "Anton", Impact, sans-serif;
    font-size: 40px;
    letter-spacing: 0.5px;
    white-space: nowrap;
  }
  .cta .free {
    font-family: "Luckiest Guy", "Arial Black", sans-serif;
    font-size: 62px;
    color: var(--yellow);
    vertical-align: -4px;
    margin: 0 4px;
  }
  .contact {
    margin: 6px 0 0;
    font-size: 27px;
    font-weight: 700;
    white-space: nowrap;
  }
</style>
</head>
<body>
<main class="poster">
  <p class="line question">Does Your Child Love to</p>
  <h2 class="line activities">
    <span class="dance">DANCE,</span> <span class="sing">SING</span><span class="amp">&amp;</span><span class="sport">PLAY SPORT?</span>
  </h2>
  <p class="line enrol">Enroll in our FUN-FILLED Program...</p>
  <h1 class="line program-name">TWIRL 'N' HOP</h1>
  <p class="line intro">A FUN Introduction to the JOY of</p>
  <p class="line disciplines">Dance, Sport <span class="and">and</span> Music</p>
  <p class="line venue">Held in Your Childcare Centre!!</p>

  <svg class="rainbow" width="846" height="500" viewBox="0 0 846 500" aria-hidden="true">
    <defs>
      <clipPath id="wave-top">
        <path d="M14 20 Q180 5 330 30 Q500 60 590 120 Q700 150 832 95 V500 H14 Z"/>
      </clipPath>
    </defs>
    <g clip-path="url(#wave-top)">
      <rect x="14" y="0" width="165" height="500" fill="var(--stripe-red)"/>
      <rect x="178" y="0" width="166" height="500" fill="var(--stripe-yellow)"/>
      <rect x="343" y="0" width="166" height="500" fill="var(--stripe-green)"/>
      <rect x="508" y="0" width="163" height="500" fill="var(--stripe-blue)"/>
      <rect x="670" y="0" width="162" height="500" fill="var(--stripe-purple)"/>
    </g>
  </svg>

  <div class="kids-area" role="img" aria-label="Silhouettes of five happy children dancing in a row"></div>

  <p class="fun-burst">FUN!</p>
  <p class="ages">For Children<br>Ages 2 to 6</p>

  <div class="price-badge">
    <span class="from">From only</span>
    <span class="amount"><sup>$</sup>10</span>
    <span class="per">per class</span>
  </div>

  <footer class="footer-band">
    <p class="cta">Sign Up for Your <span class="free">FREE</span> Trial Class Today!</p>
    <p class="contact">Phone 0400 555 019 • Email twirlnhop@funmail.com</p>
  </footer>
</main>
</body>
</html>
```